tobrin family medicine business cards

create business cards for 7 family medicine providers and 4 admin using attached logo
2 locations
appointment reminder on back of cards
will provide more info regarding names,addresses, credentials etc once started

```html
<!DOCTYPE html>
<html lang="en">
<head>
<meta charset="utf-8">
<title>Tobrin Family Medicine – Business Cards</title>
<link rel="stylesheet" href="https://fonts.googleapis.com/css2?family=Cormorant+Garamond:ital,wght@0,600;0,700;1,600;1,700&family=Lato:wght@400;700&display=swap">
<style>
  :root {
    --navy: #22236b;
    --sky: #29a9e1;
    --grey: #6b6f78;
    --paper: #ffffff;
    --backdrop: #2b2c30;
    --rule: #9aa0aa;
  }
  * { box-sizing: border-box; margin: 0; padding: 0; }
  html, body { width: 1200px; height: 952px; overflow: hidden; }
  body {
    background: var(--backdrop);
    display: flex; align-items: center; justify-content: center; gap: 32px;
    font-family: "Lato", sans-serif;
  }
  .card {
    position: relative; width: 560px; height: 320px;
    background: var(--paper); overflow: hidden;
    box-shadow: 0 10px 30px rgba(0,0,0,.45);
  }
  .brand {
    display: flex; align-items: center; gap: 10px;
    font-family: "Cormorant Garamond", serif; font-weight: 700;
    color: var(--navy); letter-spacing: .02em; line-height: 1.05;
  }
  .brand-dot { width: 18px; height: 18px; border-radius: 50%; background: var(--sky); flex: none; }

  /* Front */
  .front .brand { position: absolute; left: 30px; top: 104px; width: 220px; font-size: 24px; }
  .front .band { position: absolute; left: 0; right: 0; bottom: 0; height: 12px; background: var(--sky); }
  .front .details { position: absolute; left: 272px; right: 24px; top: 30px; }
  .doctor-name {
    font-family: "Cormorant Garamond", serif; font-weight: 700; color: var(--navy);
    font-size: 27px; line-height: 1; text-transform: uppercase; white-space: nowrap;
  }
  .doctor-name .prefix { text-transform: none; }
  .credential {
    font-family: "Cormorant Garamond", serif; font-weight: 700; color: var(--navy);
    font-size: 15px; text-align: right; margin-top: 2px;
  }
  .specialty {
    font-family: "Cormorant Garamond", serif; font-style: italic; font-weight: 600;
    color: var(--sky); font-size: 15px; margin-top: 4px;
  }
  .providers { color: var(--navy); font-size: 9.5px; line-height: 1.45; margin-top: 8px; white-space: nowrap; }
  .divider { height: 1px; background: var(--sky); margin: 9px 0 8px; width: 78%; }
  .location { color: var(--grey); font-size: 9.5px; line-height: 1.5; white-space: nowrap; }
  .location + .location { margin-top: 6px; }
  .location b { color: var(--navy); }
  .location .sep { color: var(--sky); }
  .web { color: var(--sky); font-size: 10px; line-height: 1.5; margin-top: 4px; }
  .web .navy { color: var(--navy); }

  /* Back */
  .back .decor { position: absolute; left: -70px; top: -90px; width: 300px; height: 300px; }
  .back .brand { position: absolute; right: 30px; top: 30px; font-size: 20px; }
  .reminder {
    position: absolute; right: 30px; top: 66px; text-align: right;
    font-family: "Cormorant Garamond", serif; font-style: italic; font-weight: 700;
    color: var(--sky); font-size: 19px; line-height: 1.15;
  }
  .fields { position: absolute; left: 250px; right: 30px; top: 130px; }
  .field { display: flex; align-items: flex-end; gap: 6px; color: var(--navy); font-size: 12px; margin-bottom: 16px; }
  .field .line { flex: 1; border-bottom: 1px dashed var(--rule); height: 1px; margin-bottom: 3px; }
  .back .band {
    position: absolute; left: 0; right: 0; bottom: 0; height: 58px;
    background: var(--sky); color: #fff; font-size: 13px; line-height: 1.4;
    display: flex; align-items: center; justify-content: center; text-align: center; padding: 0 40px;
  }
  .back .band strong { color: var(--navy); }
</style>
</head>
<body>
  <article class="card front">
    <div class="brand"><span class="brand-dot"></span><span>Tobrin<br>Family Medicine</span></div>
    <section class="details">
      <h1 class="doctor-name"><span class="prefix">Dr.</span> Martin Tobrin</h1>
      <div class="credential">D.O. P.A</div>
      <div class="specialty">Board Certified Family Medicine</div>
      <p class="providers">
        • Dr. Helen Tobrin, DNP • Dr. Laura Pennick<br>
        DNP Renee Dalworth, APRN • Dr. Simone Harwick<br>
        DN Paula Westerly MSN, APRN-BC<br>
        • Dr. Nadia Corvell, MD
      </p>
      <div class="divider"></div>
      <p class="location">4120 Meadow Rd. #210 Lakeside, FL 33015<br>
        <b>Phone:</b> 555-410-2231 <span class="sep">|</span> <b>Fax:</b> 555-410-2298</p>
      <p class="location">1800 W. Harbor Pkwy #105 Fairview, FL 33027<br>
        <b>Phone:</b> 555-736-1184 <span class="sep">|</span> <b>Fax:</b> 555-736-1190</p>
      <p class="web">office@tobrinclinic.com<br><span class="navy">www.</span>tobrinclinic.com</p>
    </section>
    <div class="band"></div>
  </article>

  <article class="card back">
    <svg class="decor" viewBox="0 0 300 300" aria-hidden="true">
      <circle cx="150" cy="150" r="140" fill="var(--sky)" stroke="var(--navy)" stroke-width="6"/>
    </svg>
    <div class="brand"><span class="brand-dot"></span>Tobrin Family Medicine</div>
    <p class="reminder">Your next appointment is<br>scheduled for:</p>
    <section class="fields">
      <div class="field"><span>Name :</span><span class="line"></span></div>
      <div class="field"><span>Date :</span><span class="line"></span></div>
      <div class="field"><span>Time :</span><span class="line"></span></div>
    </section>
    <div class="band">
      <p>Please give 24 hours notice for cancellations to<br>avoid a <strong>$50.00 no show fee.</strong></p>
    </div>
  </article>
</body>
</html>
```